Bidmark Display ads for Real Estate Photography

I'm looking for someone to take ideas off of my flyers and website (lensvale.example) to create two sets of display ads. One for branding and another for specific specials (see magazine-ad-special.pdf). I would like these to be animated gifs that cycle between 2 or 3 views. Here are the dimensions for the ads:
300 x 250 – Inline Rectangle
728 x 90 – Leaderboard
160 x 600 – Wide Skyscraper
320×100 - Large Mobile Banner
I can also provide source artwork from the flyers if needed.
Target Market(s)
Realtors that sell high end luxury homes
Industry/Entity Type
Professional Photography
Requirements
Must have
- .psd source files for each size ad with screens/views on different layers to I can export as an animated gif
- display ads in the following sizes:
- 300 x 250 – Inline Rectangle
- 728 x 90 – Leaderboard
- 160 x 600 – Wide Skyscraper
- 320×100 - Large Mobile Banner
Nice to have
- 336 x 280 – Large Rectangle
- 300 x 600 – Half-Page Ad

```html
<!DOCTYPE html>
<html lang="en">
<head>
<meta charset="utf-8">
<title>Lensvale Display Ads Banner Design</title>
<link href="https://fonts.googleapis.com/css2?family=Roboto:wght@300;400;500&display=swap" rel="stylesheet">
<style>
  :root {
    --board: #2a1d17;
    --board-edge: #1a120e;
    --label: #e6e1dc;
    --white: #ffffff;
    --brand-blue: #1565b0;
    --ad-blue: #0c5699;
    --band-blue: #1466ac;
    --button-blue: #1f8ad8;
    --button-edge: #5db3f0;
    --arc-blue: #2e8fdc;
  }
  * { box-sizing: border-box; margin: 0; padding: 0; }
  html, body { width: 1200px; height: 1200px; overflow: hidden; }
  body {
    background: radial-gradient(ellipse at center, #3a2a21 0%, var(--board) 60%, var(--board-edge) 100%);
    font-family: "Roboto", sans-serif;
    position: relative;
  }
  .board-frame {
    position: absolute; left: 13px; top: 13px; width: 1174px; height: 1174px;
    border: 1px solid rgba(255,255,255,0.12);
  }
  .board-title {
    position: absolute; top: 76px; left: 0; width: 1200px; text-align: center;
    color: var(--label); font-weight: 300; font-size: 29px; letter-spacing: 0.5px;
  }
  .size-label {
    position: absolute; color: var(--label); font-size: 13px; font-weight: 400;
  }
  .ad {
    position: absolute; background: var(--ad-blue); overflow: hidden;
    color: var(--white);
  }
  .ad svg.ad-art { position: absolute; left: 0; top: 0; }
  .logo-zone { position: absolute; left: 0; top: 0; background: var(--white); }
  .logo-name {
    position: absolute; color: var(--brand-blue); font-weight: 500; line-height: 1;
    white-space: nowrap;
  }
  .text-band { position: absolute; background: var(--band-blue); }
  .headline {
    position: absolute; text-align: center; text-transform: uppercase;
    font-weight: 400; line-height: 1.25; white-space: nowrap;
  }
  .cta {
    position: absolute; background: var(--button-blue);
    border: 1px solid var(--button-edge); border-radius: 3px;
    color: var(--white); text-align: center; font-weight: 400;
    box-shadow: 0 1px 2px rgba(0,0,0,0.35);
  }
</style>
</head>
<body>
  <div class="board-frame"></div>
  <h1 class="board-title">LENSVALE DISPLAY ADS BANNER DESIGN</h1>

  <svg width="0" height="0" style="position:absolute">
    <defs>
      <linearGradient id="poolScene" x1="0" y1="0" x2="0" y2="1">
        <stop offset="0" stop-color="#2c3040"/>
        <stop offset="0.3" stop-color="#6b5a48"/>
        <stop offset="0.5" stop-color="#b9b3ac"/>
        <stop offset="0.62" stop-color="#22a8e6"/>
        <stop offset="0.85" stop-color="#0e78c0"/>
        <stop offset="1" stop-color="#4a4e56"/>
      </linearGradient>
    </defs>
  </svg>

  <!-- Leaderboard 728x90 -->
  <span class="size-label" style="left:213px;top:208px">728-90</span>
  <div class="ad ad-leaderboard" style="left:213.6px;top:236.8px;width:582.4px;height:72px">
    <svg class="ad-art" width="582.4" height="72">
      <rect x="117" y="0" width="127" height="72" fill="#0f5da3"/>
      <path d="M368,0 Q354,36 368,72" fill="none" stroke="var(--arc-blue)" stroke-width="6"/>
      <path d="M375,0 Q362,36 375,72 L582.4,72 L582.4,0 Z" fill="url(#poolScene)" role="img" aria-label="Photo of a luxury home with arched terrace and lit pool at dusk"/>
    </svg>
    <div class="logo-zone" style="width:117px;height:72px"></div>
    <div class="logo-name" style="left:10px;top:26px;font-size:22px">Lensvale</div>
    <div class="headline" style="left:117px;top:14px;width:127px;font-size:12px">Grow your<br>business &amp; sell<br>more homes</div>
    <div class="cta" style="left:262px;top:24.8px;width:90px;height:26px;line-height:24px;font-size:12.5px">Learn More</div>
  </div>

  <!-- Inline Rectangle 300x250 -->
  <span class="size-label" style="left:212px;top:344px">300-250</span>
  <div class="ad" style="left:213.6px;top:365.6px;width:240px;height:200px">
    <div class="logo-zone" style="width:150px;height:42px"></div>
    <div class="text-band" style="left:0;top:64px;width:150px;height:76px"></div>
    <svg class="ad-art" width="240" height="200">
      <path d="M133,0 Q85,100 133,200" fill="none" stroke="var(--arc-blue)" stroke-width="6"/>
      <path d="M140,0 Q92,100 140,200 L240,200 L240,0 Z" fill="url(#poolScene)" role="img" aria-label="Photo of a luxury home with arched terrace and lit pool at dusk"/>
    </svg>
    <div class="logo-name" style="left:9px;top:9px;font-size:24px">Lensvale</div>
    <div class="headline" style="left:0;top:84px;width:132px;font-size:12px">Grow your<br>business &amp; sell<br>more homes</div>
    <div class="cta" style="left:9px;top:159px;width:90px;height:26px;line-height:24px;font-size:12.5px">Click Here</div>
  </div>

  <!-- Large Rectangle 336x280 -->
  <span class="size-label" style="left:212px;top:600px">336-280</span>
  <div class="ad" style="left:212.8px;top:621.6px;width:268.8px;height:224px">
    <div class="logo-zone" style="width:180px;height:58px"></div>
    <div class="text-band" style="left:0;top:80px;width:160px;height:76px"></div>
    <svg class="ad-art" width="268.8" height="224">
      <path d="M163,0 Q103,130 156,224" fill="none" stroke="var(--arc-blue)" stroke-width="6"/>
      <path d="M170,0 Q110,130 163,224 L268.8,224 L268.8,0 Z" fill="url(#poolScene)" role="img" aria-label="Photo of a luxury home with arched terrace and lit pool at dusk"/>
    </svg>
    <div class="logo-name" style="left:10px;top:14px;font-size:30px">Lensvale</div>
    <div class="headline" style="left:0;top:96px;width:145px;font-size:13.5px">Grow your<br>business &amp; sell<br>more homes</div>
    <div class="cta" style="left:17px;top:178px;width:90px;height:26px;line-height:24px;font-size:12.5px">Click Here</div>
  </div>

  <!-- Wide Skyscraper 160x600 -->
  <span class="size-label" style="left:532px;top:344px">160-600</span>
  <div class="ad" style="left:531.2px;top:365.6px;width:128px;height:480px">
    <div class="logo-zone" style="width:128px;height:56px"></div>
    <div class="text-band" style="left:0;top:56px;width:128px;height:110px"></div>
    <svg class="ad-art" width="128" height="480">
      <path d="M0,284 Q64,260 128,284" fill="none" stroke="var(--arc-blue)" stroke-width="6"/>
      <path d="M0,290 Q64,266 128,290 L128,480 L0,480 Z" fill="url(#poolScene)" role="img" aria-label="Photo of a luxury home with arched terrace and lit pool at dusk"/>
    </svg>
    <div class="logo-name" style="left:11px;top:16px;font-size:25px">Lensvale</div>
    <div class="headline" style="left:0;top:81px;width:128px;font-size:13.5px;line-height:1.45">Grow your<br>business &amp; sell<br>more homes</div>
    <div class="cta" style="left:19px;top:185px;width:90px;height:26px;line-height:24px;font-size:12.5px">Click Here</div>
  </div>

  <!-- Half-Page 300x600 -->
  <span class="size-label" style="left:704px;top:344px">300-600</span>
  <div class="ad" style="left:706.4px;top:365.6px;width:240px;height:480px">
    <div class="logo-zone" style="width:240px;height:54px"></div>
    <div class="text-band" style="left:0;top:54px;width:240px;height:130px"></div>
    <svg class="ad-art" width="240" height="480">
      <path d="M0,293 Q120,223 240,293" fill="none" stroke="var(--arc-blue)" stroke-width="6"/>
      <path d="M0,300 Q120,230 240,300 L240,480 L0,480 Z" fill="url(#poolScene)" role="img" aria-label="Photo of a luxury home with arched terrace and lit pool at dusk"/>
    </svg>
    <div class="logo-name" style="left:0;width:240px;text-align:center;top:13px;font-size:29px">Lensvale</div>
    <div class="headline" style="left:0;top:67px;width:240px;font-size:24.5px;line-height:1.38">Grow your<br>business &amp; sell<br>more homes</div>
    <div class="cta" style="left:67px;top:207px;width:106px;height:28px;line-height:26px;font-size:13px">Click Here</div>
  </div>

  <!-- Large Mobile Banner 320x100 -->
  <span class="size-label" style="left:212px;top:880px">320×100</span>
  <div class="ad" style="left:212.8px;top:907.2px;width:256px;height:80px">
    <div class="logo-zone" style="width:120px;height:29px"></div>
    <svg class="ad-art" width="256" height="80">
      <path d="M111,0 Q106,40 111,80" fill="none" stroke="var(--arc-blue)" stroke-width="4"/>
      <path d="M116,0 Q111,40 116,80 L256,80 L256,0 Z" fill="url(#poolScene)" role="img" aria-label="Photo of a luxury home with arched terrace and lit pool at dusk"/>
    </svg>
    <div class="logo-name" style="left:0;width:115px;text-align:center;top:6px;font-size:17px">Lensvale</div>
    <div class="headline" style="left:0;top:34px;width:114px;font-size:8.5px;font-weight:500;line-height:1.25">Grow your business<br>&amp; sell more homes</div>
    <div class="cta" style="left:27px;top:59px;width:58px;height:17px;line-height:15px;font-size:7.5px">Click Here</div>
  </div>
</body>
</html>
```